Business Card Design
Brightvale Marks
Modern
Kemi Varo
47 Olumide Bankole Crescent
Wuse 2
Abuja
Nigeria
info@brightvalemarks.com
www.brightvalemarks.com

```html
<!DOCTYPE html>
<html lang="en">
<head>
<meta charset="utf-8">
<title>Brightvale Marks — Business Card</title>
<link rel="stylesheet" href="https://fonts.googleapis.com/css2?family=Tinos:wght@400&display=swap">
<style>
  :root {
    --backdrop: #7b93c9;
    --card: #ffffff;
    --ink: #2b2b2b;
    --brand-blue: #2f7fc4;
    --brand-green: #8cc63f;
    --band-green: #b9dc84;
    --band-blue: #a9d8f2;
    --icon-blue: #3a8fd0;
  }
  * { margin: 0; padding: 0; box-sizing: border-box; }
  html, body { width: 1200px; height: 890px; overflow: hidden; }
  body {
    background: var(--backdrop);
    font-family: "Tinos", "Times New Roman", serif;
    color: var(--ink);
    position: relative;
  }
  .card {
    position: absolute;
    width: 600px;
    height: 340px;
    background: var(--card);
    box-shadow: 0 6px 18px rgba(0,0,0,0.18);
  }
  /* Front face */
  .card--front { left: 60px; top: 90px; }
  .front-lockup {
    position: absolute; left: 0; right: 0; top: 0; bottom: 0;
    display: flex; flex-direction: column; align-items: center; justify-content: center;
    gap: 18px;
  }
  .brand-dot {
    width: 110px; height: 110px; border-radius: 50%;
    background: var(--brand-green);
  }
  .brand-name {
    font-size: 40px; letter-spacing: 2px; text-transform: uppercase;
    color: var(--brand-blue);
  }
  /* Back face */
  .card--back { left: 540px; top: 470px; }
  .band { position: absolute; top: 0; bottom: 0; }
  .band--left { left: 0; width: 46px; }
  .band--right { right: 0; width: 52px; }
  .holder-name {
    position: absolute; left: 64px; top: 26px;
    font-size: 26px; text-transform: uppercase; letter-spacing: 1px;
  }
  .company-block {
    position: absolute; left: 170px; top: 96px;
    display: flex; gap: 16px; align-items: flex-start;
  }
  .company-dot {
    width: 90px; height: 90px; border-radius: 50%;
    background: var(--brand-green); flex: none; margin-top: 4px;
  }
  .company-name {
    font-size: 24px; text-transform: uppercase; color: var(--ink); line-height: 1.1;
  }
  .company-address { font-size: 19px; line-height: 1.25; }
  .contact-list {
    position: absolute; left: 290px; top: 220px; list-style: none;
    font-size: 19px;
  }
  .contact-list li { display: flex; align-items: center; gap: 8px; height: 30px; }
  .contact-icon { width: 22px; height: 22px; flex: none; }
</style>
</head>
<body>
  <section class="card card--front" aria-label="Card front">
    <div class="front-lockup">
      <span class="brand-dot" aria-hidden="true"></span>
      <span class="brand-name">Brightvale Marks</span>
    </div>
  </section>

  <section class="card card--back" aria-label="Card back">
    <svg class="band band--left" viewBox="0 0 46 340" preserveAspectRatio="none" aria-hidden="true">
      <polygon points="0,0 46,34 46,306 0,340" fill="var(--band-green)"/>
    </svg>
    <svg class="band band--right" viewBox="0 0 52 340" preserveAspectRatio="none" aria-hidden="true">
      <polygon points="0,34 52,0 52,340 0,306" fill="var(--band-blue)"/>
    </svg>

    <h1 class="holder-name">Kemi Varo</h1>

    <div class="company-block">
      <span class="company-dot" aria-hidden="true"></span>
      <div>
        <div class="company-name">Brightvale Marks</div>
        <address class="company-address" style="font-style:normal">
          47 Olumide Bankole Crescent<br>
          Wuse 2, Abuja, Nigeria
        </address>
      </div>
    </div>

    <ul class="contact-list">
      <li>
        <svg class="contact-icon" viewBox="0 0 24 24" aria-hidden="true">
          <circle cx="12" cy="12" r="10.5" fill="none" stroke="var(--icon-blue)" stroke-width="1.6"/>
          <path d="M8.5 7c.6-.6 1.4-.4 1.7.3l.8 1.8c.2.5 0 1-.4 1.3l-.6.5c.6 1.3 1.6 2.3 2.9 2.9l.5-.6c.3-.4.8-.6 1.3-.4l1.8.8c.7.3.9 1.1.3 1.7l-.8.8c-.8.8-2.2.7-4-.4-1.6-1-3-2.4-4-4-1.1-1.8-1.2-3.2-.4-4z" fill="var(--icon-blue)"/>
        </svg>
        08140057219
      </li>
      <li>
        <svg class="contact-icon" viewBox="0 0 24 24" aria-hidden="true">
          <circle cx="12" cy="12" r="10.5" fill="none" stroke="var(--icon-blue)" stroke-width="1.6"/>
          <rect x="6.5" y="8" width="11" height="8" rx="1" fill="none" stroke="var(--icon-blue)" stroke-width="1.4"/>
          <path d="M6.8 8.4 12 12.5l5.2-4.1" fill="none" stroke="var(--icon-blue)" stroke-width="1.4"/>
        </svg>
        info@brightvalemarks.com
      </li>
      <li>
        <svg class="contact-icon" viewBox="0 0 24 24" aria-hidden="true">
          <circle cx="12" cy="12" r="10.5" fill="var(--icon-blue)"/>
          <g fill="none" stroke="#fff" stroke-width="1.2">
            <circle cx="12" cy="12" r="6.5"/>
            <ellipse cx="12" cy="12" rx="3" ry="6.5"/>
            <path d="M5.5 12h13M6.5 8.7h11M6.5 15.3h11"/>
          </g>
        </svg>
        www.brightvalemarks.com
      </li>
    </ul>
  </section>
</body>
</html>
```